Bright Path Flyer Design for Virtual Online Clinic. -5.5 x 8.5 inches (half sheet)

We need a clean, modern flyer design for Bright Path, a new virtual walk-in clinic based in British Columbia. The flyer will be used in libraries, pharmacies, and community centers to help residents easily access primary care through their Bright Path NFC access card.
The flyer will ask a question : NEED A DOCTOR? This should be large and attention grabbing.
The design should clearly feature a Bright Path card image (the access card) as the centerpiece and visually show how patients can use it to book appointments. The tone should feel trustworthy, healthcare-oriented, and community-friendly — clean fonts, clear spacing, and strong readability from a distance.

Side One: This card has the NFC Access Card.
NEED A DOCTOR? (Large Font, Attention Grabbing)
How to Book an Appointment using your Bright Path Card
Step 1: Tap Your Card on Your Phone
Hold your card near the back of your phone.
It will activate automatically — no app needed.
The Bright Path scheduler will open.
Step 2: Schedule Your Appointment
Select your clinical concern.
Choose your time window.
Register (only once).
Confirm your appointment.
Step 3: Relax, we’ll take care of the rest
A doctor will call during your scheduled time.
Once booked, you’ll be able to call our office.
No emails, no texts — just a real person.
It’s that simple.
Side Two:
About Bright Path
Created by Dr. Marcus Ferrigan
Bright Path was founded to make healthcare simple and convenient. Prescription renewals. Common infections. Medical notes. And so much more.
Our doctors can address 120+ health concerns virtually — providing quality care without the waiting room. No waiting rooms. Just real doctors providing real care.
Why Patients Choose Bright Path
Easy access – book and be seen from anywhere in BC.
Effortless booking – tap your Bright Path Card to begin.
Trusted physicians – every visit is with a licensed BC family doctor.
How It Works
Book your visit — choose a time window that fits your day.
Join the queue — you’ll be called when it’s your turn.
Speak directly with your doctor — simple, secure, and stress-free.
Convenient Care for Common Concerns

Additional Details.
Please find the domain to be launched soon. I've attached the NFC card file for review, it is 85.5 mm x 54 mm. The card will be glued to the flyer.
I've attached examples of flyers but they are not the look I am seeking and I am looking for creative solutions.
Thank you!
http://brightpath-example.test/

Adult Patients in British Columbia

Healthcare

• Looking for clean lines, uniform appearance, and high legibility i.e poppins

0054AA
0677BA
7BADD7
CADEEF
E8F1F8

• Need A Doctor?
• Elegant style, not too busy, clear layout.
• Clutter, look cheap - review examples.

```html
<!DOCTYPE html>
<html lang="en">
<head>
<meta charset="utf-8">
<title>Bright Path Flyer</title>
<link href="https://fonts.googleapis.com/css2?family=Poppins:wght@400;500;600;700;800&display=swap" rel="stylesheet">
<style>
  :root{
    --navy:#0054AA;
    --blue:#0677BA;
    --sky:#7BADD7;
    --cyan:#3FC3DE;
    --mist:#CADEEF;
    --ice:#E8F1F8;
    --green:#19B985;
    --ink:#2f3a46;
    --grey:#5b6673;
    --page:#f7f9fc;
    --stage:#dfe6ec;
  }
  *{box-sizing:border-box;margin:0;padding:0}
  html,body{width:1200px;height:1200px;overflow:hidden}
  body{background:var(--stage);font-family:'Poppins',sans-serif;position:relative}
  .flyer{position:absolute;top:182px;width:540px;height:835px;background:var(--page);overflow:hidden;box-shadow:0 8px 28px rgba(0,40,80,.18)}
  .flyer--front{left:40px}
  .flyer--back{left:620px}
  .flyer__band{position:absolute;inset:0}
  .brand{position:absolute;top:24px;font-size:26px;font-weight:500;color:var(--navy);letter-spacing:.5px}
  .flyer--front .brand{left:36px}
  .flyer--back .brand{right:36px}

  .headline{position:absolute;left:30px;top:140px;color:#fff;font-size:58px;font-weight:800;line-height:1.02}
  .portrait{position:absolute;left:312px;top:110px;width:200px;height:318px;border-radius:100px;border:4px solid var(--cyan);outline:4px solid #fff;background:linear-gradient(170deg,#4fd1a8 0%,#dde9f2 60%,#f5f8fb 100%)}

  .booking-title{position:absolute;left:30px;top:395px;font-size:26px;font-weight:700;line-height:1.3;color:var(--blue);white-space:nowrap}
  .booking-title .highlight{display:inline-block;background:var(--cyan);color:#fff;padding:0 12px;border-radius:12px;margin-left:-6px}
  .booking-title .accent{color:var(--navy)}

  .steps{position:absolute;left:30px;top:512px;width:470px;list-style:none}
  .step{display:flex;gap:18px;margin-bottom:10px}
  .step__icon{flex:0 0 52px;height:52px;border-radius:50%;display:flex;align-items:center;justify-content:center}
  .step__icon--green{background:var(--green)}
  .step__icon--cyan{background:var(--cyan)}
  .step__icon--navy{background:var(--navy)}
  .step__title{font-size:13px;font-weight:600;color:var(--ink);line-height:1.4}
  .step__text{font-size:11px;color:var(--grey);line-height:1.4}

  .rule{position:absolute;left:30px;right:230px;bottom:45px;height:1.5px;background:var(--blue)}
  .url-pill{position:absolute;right:30px;bottom:30px;background:var(--navy);color:#fff;font-size:12.5px;font-weight:500;padding:6px 16px;border-radius:16px;border:2px solid var(--sky)}

  .about-title{position:absolute;left:0;right:0;top:120px;text-align:center;color:#fff;font-size:40px;font-weight:800;line-height:1.1;letter-spacing:2px}
  .creator-pill{position:absolute;left:50%;top:240px;transform:translateX(-50%);background:var(--cyan);color:#fff;text-align:center;padding:10px 30px;border-radius:30px;white-space:nowrap}
  .creator-pill small{display:block;font-size:11px;font-weight:500;letter-spacing:1.5px}
  .creator-pill strong{font-size:16px;font-weight:700;letter-spacing:1px}
  .about-text{position:absolute;left:40px;right:40px;top:355px;text-align:center;font-size:12.5px;font-weight:500;color:var(--ink);line-height:1.5}
  .section-bar{position:absolute;left:30px;right:30px;background:var(--green);color:#fff;font-size:19px;font-weight:700;text-align:center;padding:5px 0;border-radius:10px}
  .section-bar--why{top:482px}
  .section-bar--how{top:610px}
  .point-list{position:absolute;left:40px;right:40px;list-style:none;font-size:12px;font-weight:500;color:var(--ink);line-height:1.6}
  .point-list--why{top:530px}
  .point-list--how{top:658px}
</style>
</head>
<body>

<section class="flyer flyer--front">
  <svg class="flyer__band" width="540" height="835" viewBox="0 0 540 835" aria-hidden="true">
    <defs>
      <linearGradient id="frontBand" x1="0" y1="0" x2="1" y2="0">
        <stop offset="0" stop-color="#0054AA"/>
        <stop offset="0.55" stop-color="#0677BA"/>
        <stop offset="1" stop-color="#3FC3DE"/>
      </linearGradient>
    </defs>
    <polygon points="0,80 540,80 540,465 0,330" fill="url(#frontBand)"/>
  </svg>

  <div class="brand">Bright Path</div>
  <h1 class="headline">Need a<br>Doctor?</h1>
  <div class="portrait" role="img" aria-label="Photo of two smiling doctors in white coats with stethoscopes"></div>

  <h2 class="booking-title">How to Book<br><span class="highlight">an Appointment</span><br><span class="accent">using your Bright Path Card</span></h2>

  <ol class="steps">
    <li class="step">
      <span class="step__icon step__icon--green">
        <svg width="28" height="28" viewBox="0 0 28 28" fill="none" stroke="#fff" stroke-width="2"><rect x="3" y="7" width="22" height="14" rx="2"/><line x1="3" y1="12" x2="25" y2="12"/><line x1="7" y1="17" x2="12" y2="17"/></svg>
      </span>
      <div>
        <p class="step__title">Step 1: Tap Your Card on Your Phone</p>
        <p class="step__text">Hold your card near the back of your phone.<br>It will activate automatically — no app needed.<br>The Bright Path scheduler will open.</p>
      </div>
    </li>
    <li class="step">
      <span class="step__icon step__icon--cyan">
        <svg width="28" height="28" viewBox="0 0 28 28" fill="none" stroke="#fff" stroke-width="2"><rect x="4" y="6" width="20" height="18" rx="2"/><line x1="4" y1="11" x2="24" y2="11"/><line x1="9" y1="3" x2="9" y2="8"/><line x1="19" y1="3" x2="19" y2="8"/><polyline points="10,17 13,20 18,14"/></svg>
      </span>
      <div>
        <p class="step__title">Step 2: Schedule Your Appointment</p>
        <p class="step__text">Select your clinical concern.<br>Choose your time window.<br>Register (only once).<br>Confirm your appointment.</p>
      </div>
    </li>
    <li class="step">
      <span class="step__icon step__icon--navy">
        <svg width="28" height="28" viewBox="0 0 28 28" fill="none" stroke="#fff" stroke-width="2"><path d="M8 4h4l2 5-3 2a11 11 0 0 0 6 6l2-3 5 2v4a2 2 0 0 1-2 2A18 18 0 0 1 6 6a2 2 0 0 1 2-2z"/></svg>
      </span>
      <div>
        <p class="step__title">Step 3: Relax, we’ll take care of the rest</p>
        <p class="step__text">A doctor will call during your scheduled time.<br>Once booked, you’ll be able to call our office.<br>No emails, no texts — just a real person.<br>It’s that simple.</p>
      </div>
    </li>
  </ol>

  <div class="rule"></div>
  <div class="url-pill">http://brightpath-example.test/</div>
</section>

<section class="flyer flyer--back">
  <svg class="flyer__band" width="540" height="835" viewBox="0 0 540 835" aria-hidden="true">
    <defs>
      <linearGradient id="backBand" x1="0" y1="0" x2="1" y2="1">
        <stop offset="0" stop-color="#0054AA"/>
        <stop offset="1" stop-color="#3FC3DE"/>
      </linearGradient>
    </defs>
    <rect x="0" y="80" width="540" height="250" fill="url(#backBand)"/>
  </svg>

  <div class="brand">Bright Path</div>
  <h1 class="about-title">ABOUT<br>BRIGHT PATH</h1>
  <div class="creator-pill"><small>CREATED BY:</small><strong>DR. MARCUS FERRIGAN</strong></div>

  <p class="about-text">Bright Path was founded to make healthcare simple and convenient. Prescription renewals. Common infections. Medical notes. And so much more. Our doctors can address 120+ health concerns virtually — providing quality care without the waiting room. No waiting rooms. Just real doctors providing real care.</p>

  <h2 class="section-bar section-bar--why">Why Patients Choose Bright Path</h2>
  <ul class="point-list point-list--why">
    <li>Easy access – book and be seen from anywhere in BC.</li>
    <li>Effortless booking – tap your Bright Path Card to begin.</li>
    <li>Trusted physicians – every visit is with a licensed BC family doctor.</li>
  </ul>

  <h2 class="section-bar section-bar--how">How It Works</h2>
  <ul class="point-list point-list--how">
    <li>Book your visit — choose a time window that fits your day.</li>
    <li>Join the queue — you’ll be called when it’s your turn.</li>
    <li>Speak directly with your doctor — simple, secure, and stress-free.</li>
    <li>Convenient Care for Common Concerns.</li>
  </ul>

  <div class="rule"></div>
  <div class="url-pill">http://brightpath-example.test/</div>
</section>

</body>
</html>
```